Wren's Velvet Lantern Soiree

We need an invitation that compliments a start studded guest list of the most influential 20-30 year olds in manhattan. The theme of the party is moroccan nights with black and gold color scheme. 9pm - all night, cocktails and horderves followed by Dj Pollux and surprise entertainment. Attire gypsy chic. Address will be provided upon RSVP

Font styles to use
Decorative
Script

Colors
fbed22
000000

Requirements
Should not have
• basic

```html
<!DOCTYPE html>
<html lang="en">
<head>
<meta charset="utf-8">
<title>Wren's Velvet Lantern Soiree – Invitation</title>
<link rel="stylesheet" href="https://fonts.googleapis.com/css2?family=PT+Sans+Narrow:wght@400;700&display=swap">
<style>
  :root {
    --paper: #ffffff;
    --card: #000000;
    --gold: #c99a45;
    --trim: #4a4a4a;
  }
  * { margin: 0; padding: 0; box-sizing: border-box; }
  html, body {
    width: 927px;
    height: 1200px;
    overflow: hidden;
    background: var(--paper);
  }
  .sheet {
    position: relative;
    width: 927px;
    height: 1200px;
  }
  .crop-marks {
    position: absolute;
    inset: 0;
  }
  .invitation {
    position: absolute;
    left: 292px;
    top: 270px;
    width: 340px;
    height: 660px;
    background: var(--card);
    color: var(--gold);
    font-family: "PT Sans Narrow", "Arial Narrow", sans-serif;
    text-align: center;
    text-transform: uppercase;
  }
  .ornament {
    position: absolute;
    left: 89px;
    top: 77px;
    width: 161px;
    height: 160px;
    background: radial-gradient(circle, #8a6a30 0%, #3a2c12 70%, var(--card) 100%);
  }
  .title {
    position: absolute;
    left: 0; right: 0;
    top: 277px;
    font-size: 22px;
    font-weight: 700;
    letter-spacing: 0.2px;
  }
  .rule {
    position: absolute;
    left: 87px;
    width: 164px;
    height: 2px;
    background: var(--gold);
  }
  .rule--top { top: 325px; }
  .rule--bottom { top: 377px; }
  .time {
    position: absolute;
    left: 0; right: 0;
    top: 335px;
    font-size: 28px;
    font-weight: 700;
  }
  .place {
    position: absolute;
    left: 0; right: 0;
    top: 390px;
    font-size: 10px;
    font-weight: 700;
  }
  .programme {
    position: absolute;
    left: 0; right: 0;
    top: 426px;
    font-size: 17px;
    line-height: 25.5px;
  }
  .details {
    position: absolute;
    left: 0; right: 0;
    top: 552px;
    font-size: 11px;
    line-height: 21px;
  }
</style>
</head>
<body>
<div class="sheet">
  <svg class="crop-marks" width="927" height="1200" aria-hidden="true">
    <g stroke="var(--trim)" stroke-width="1">
      <line x1="301.5" y1="247" x2="301.5" y2="280"/>
      <line x1="622.5" y1="247" x2="622.5" y2="280"/>
      <line x1="301.5" y1="920" x2="301.5" y2="952"/>
      <line x1="622.5" y1="920" x2="622.5" y2="952"/>
      <line x1="270" y1="279.5" x2="302" y2="279.5"/>
      <line x1="622" y1="279.5" x2="655" y2="279.5"/>
      <line x1="270" y1="920.5" x2="302" y2="920.5"/>
      <line x1="622" y1="920.5" x2="655" y2="920.5"/>
    </g>
  </svg>

  <section class="invitation">
    <div class="ornament" role="img" aria-label="Gold Moroccan lattice ornament of four interlocking star-arch tiles"></div>

    <h1 class="title">Moroccan Nights</h1>
    <div class="rule rule--top"></div>
    <p class="time">9PM - All Night</p>
    <div class="rule rule--bottom"></div>
    <p class="place">Hamptons, New York</p>

    <p class="programme">
      Cocktails and hors d'oeuvres<br>
      followed by DJ Pollux and<br>
      surprise entertainment<br>
      Required attire: gypsy chic
    </p>

    <p class="details">
      Address will be provided upon RSVP<br>
      RSVP: rsvp@velvetlanternsoiree.com
    </p>
  </section>
</div>
</body>
</html>
```